LongForm Landing Page for Quitting Smoking Device - Sales Product Page Shopify Bootstrap

Our website is https://velmora.com/ we are looking to design a landing page for our flagship product the BreathTab. Here is the product page we have currently, it is poorly laid out but has much of the info we would like to see, though more info can be found under the BreathTab menu pages. https://velmora.com/collections/frontpage/products/breathtab-stop-smoking-program-bu-velmora
We would like this be a long form sales page that traffic is driven directly to it from ads. Bootstrap 4 will be used to help code to the page so a design that takes that (such as 12 columns) into account would be appreciated. The design should be responsive.
Another source of inspiration is our other site we used to inform people about our product: http://breathtab.com/
Your design can have placeholders (provide a description of it) for images
Industry/Entity Type
Product
Number of Pages Required
1 page
Look and feel
Each slider illustrates characteristics of the customer's brand and the style your logo design should communicate.

```html
<!DOCTYPE html>
<html lang="en">
<head>
<meta charset="utf-8">
<title>Velmora – BreathTab Landing Page</title>
<link rel="stylesheet" href="https://fonts.googleapis.com/css2?family=Poppins:wght@400;500;600&display=swap">
<style>
  :root {
    --green: #8cc63f;
    --green-dark: #6fa82a;
    --ink: #222222;
    --text: #555555;
    --muted: #8a8a8a;
    --bar: #151515;
    --white: #ffffff;
    --line: #e6e6e6;
    --sky-top: #c9dbe8;
    --sky-mid: #e9f0f5;
    --dark-band: #2b2f33;
    --page-bg: #eef1f3;
  }
  * { box-sizing: border-box; margin: 0; padding: 0; }
  html, body { width: 1200px; height: 1000px; overflow: hidden; }
  body {
    font-family: "Poppins", sans-serif;
    background: var(--page-bg);
    color: var(--text);
  }
  .page { width: 1200px; height: 1000px; background: var(--white); overflow: hidden; }
  .container { width: 980px; margin: 0 auto; }

  /* Top bar */
  .topbar { background: var(--bar); height: 38px; color: #cfcfcf; font-size: 12px; }
  .topbar .container { display: flex; align-items: center; justify-content: space-between; height: 100%; }
  .topbar .call { display: flex; align-items: center; gap: 6px; }
  .topbar .call strong { color: var(--green); font-weight: 500; }
  .topbar .guarantee { display: flex; align-items: center; gap: 6px; }
  .cart-btn {
    background: var(--green); color: var(--white); height: 38px; padding: 0 22px;
    display: flex; align-items: center; gap: 8px; font-size: 12px;
  }

  /* Header */
  .site-header { height: 74px; border-bottom: 1px solid var(--line); }
  .site-header .container { display: flex; align-items: center; height: 100%; }
  .brand { display: flex; align-items: center; gap: 8px; font-size: 26px; font-weight: 600; color: var(--green-dark); }
  .brand-dot { width: 12px; height: 12px; border-radius: 50%; background: var(--green); }
  .main-nav { margin-left: auto; display: flex; gap: 28px; font-size: 13px; font-weight: 500; color: #444; }
  .main-nav a { color: inherit; text-decoration: none; position: relative; padding: 26px 0; }
  .main-nav a.active { color: var(--green); }
  .main-nav a.active::after { content: ""; position: absolute; left: -6px; right: -6px; bottom: 0; height: 2px; background: var(--green); }
  .account { margin-left: 44px; font-size: 13px; color: var(--muted); display: flex; align-items: center; gap: 4px; }
  .account .login { color: var(--green); }

  /* Hero */
  .hero { position: relative; height: 360px; }
  .hero-photo {
    position: absolute; inset: 0;
    background: linear-gradient(180deg, var(--sky-top) 0%, var(--sky-mid) 55%, #f7f9fb 100%);
  }
  .hero-people {
    position: absolute; right: 190px; top: 8px; width: 260px; height: 352px;
    border-radius: 130px 130px 0 0;
    background: linear-gradient(180deg, #e8e3dc 0%, #f4f1ec 100%);
  }
  .hero .container { position: relative; padding-top: 90px; }
  .hero-title { font-size: 22px; font-weight: 600; color: var(--ink); line-height: 1.3; }
  .hero-subtitle { font-size: 24px; font-weight: 400; color: var(--ink); line-height: 1.3; }
  .hero-text { font-size: 13px; color: #333; margin-top: 12px; width: 330px; line-height: 1.5; }
  .btn {
    display: inline-block; font-family: inherit; font-size: 12px; font-weight: 500;
    padding: 9px 22px; border: 0; text-decoration: none;
  }
  .btn-green { background: var(--green); color: var(--white); }
  .btn-outline { background: var(--white); color: #444; border: 1px solid #ddd; }
  .hero .btn { margin-top: 22px; }

  /* Product */
  .product { padding: 28px 0 30px; }
  .product .container { display: grid; grid-template-columns: 310px 1fr; gap: 40px; }
  .product-media { position: relative; }
  .media-tab {
    background: var(--bar); color: var(--white); font-size: 11px; font-weight: 500;
    padding: 8px 14px; display: inline-block;
  }
  .product-photo {
    height: 200px;
    background: linear-gradient(160deg, #f5efe9 0%, #d9c2ad 60%, #8c8c8c 100%);
  }
  .product-title { font-size: 22px; font-weight: 500; color: var(--ink); margin-top: 34px; }
  .product-text { font-size: 13px; line-height: 1.6; margin-top: 8px; max-width: 560px; }
  .price { margin-top: 12px; font-size: 14px; }
  .price s { color: var(--muted); margin-right: 6px; }
  .price .sale { color: var(--green); font-weight: 500; }
  .product-actions { display: flex; gap: 12px; margin-top: 14px; align-items: center; }
  .share { display: flex; gap: 6px; margin-top: 16px; align-items: center; font-size: 11px; color: var(--muted); }
  .share span.sq { width: 16px; height: 16px; background: #c7c7c7; display: inline-block; }

  /* Benefits */
  .benefits { background: var(--dark-band); padding: 24px 0 0; height: 300px; }
  .benefits-heading { text-align: center; color: var(--white); font-size: 17px; font-weight: 500; line-height: 1.4; }
  .benefit-card {
    background: var(--white); width: 760px; margin: 18px auto 0; padding: 18px 30px;
    display: grid; grid-template-columns: 1fr 1fr; gap: 14px 40px; border-top: 3px solid var(--green);
  }
  .benefit { display: flex; gap: 10px; }
  .benefit-icon { flex: none; width: 22px; height: 22px; }
  .benefit h3 { font-size: 13px; font-weight: 600; color: var(--ink); }
  .benefit p { font-size: 11px; color: var(--muted); }
  .how-title { text-align: center; color: #d0d0d0; font-size: 14px; margin-top: 16px; }
</style>
</head>
<body>
<div class="page">

  <div class="topbar">
    <div class="container">
      <div class="call">
        <svg width="12" height="12" viewBox="0 0 24 24" aria-hidden="true"><path fill="#8cc63f" d="M6.6 10.8a15.1 15.1 0 0 0 6.6 6.6l2.2-2.2a1 1 0 0 1 1-.25 11.4 11.4 0 0 0 3.6.57 1 1 0 0 1 1 1V20a1 1 0 0 1-1 1A17 17 0 0 1 3 4a1 1 0 0 1 1-1h3.5a1 1 0 0 1 1 1c0 1.25.2 2.45.57 3.57a1 1 0 0 1-.25 1z"/></svg>
        <strong>Call Us:</strong> 1-800-555-0192
      </div>
      <div class="guarantee">
        <svg width="12" height="12" viewBox="0 0 24 24" aria-hidden="true"><path fill="#8cc63f" d="M2 21h4V9H2zm20-11a2 2 0 0 0-2-2h-6.3l1-4.6v-.3a1.5 1.5 0 0 0-.44-1L13.2 1 6.6 7.6A2 2 0 0 0 6 9v10a2 2 0 0 0 2 2h9a2 2 0 0 0 1.84-1.22l3-7.05A2 2 0 0 0 22 12z"/></svg>
        30 Day Money Back Guarantee
      </div>
      <div class="cart-btn">
        <svg width="12" height="12" viewBox="0 0 24 24" aria-hidden="true"><path fill="#fff" d="M7 18a2 2 0 1 0 0 4 2 2 0 0 0 0-4zm10 0a2 2 0 1 0 0 4 2 2 0 0 0 0-4zM1 2v2h2l3.6 7.6L5.2 14A2 2 0 0 0 7 17h12v-2H7.4l1.1-2h7.4a2 2 0 0 0 1.75-1l3.6-6.5A1 1 0 0 0 20.4 4H5.2l-.9-2z"/></svg>
        Cart $0.00
      </div>
    </div>
  </div>

  <header class="site-header">
    <div class="container">
      <div class="brand"><span class="brand-dot"></span>Velmora</div>
      <nav class="main-nav">
        <a class="active" href="#">Home</a>
        <a href="#">BreathTab</a>
        <a href="#">MealPace</a>
        <a href="#">RestTab</a>
        <a href="#">Contact Us</a>
      </nav>
      <div class="account">
        <svg width="11" height="11" viewBox="0 0 24 24" aria-hidden="true"><circle cx="12" cy="8" r="5" fill="#8cc63f"/><path fill="#8cc63f" d="M2 22a10 8 0 0 1 20 0z"/></svg>
        <span class="login">Login</span> | Register
      </div>
    </div>
  </header>

  <section class="hero">
    <div class="hero-photo" role="img" aria-label="Photo placeholder: smiling couple embracing outdoors against a bright cloudy sky"></div>
    <div class="hero-people" role="img" aria-label="Placeholder for the embracing couple in white summer clothes"></div>
    <div class="container">
      <h1 class="hero-title">Velmora</h1>
      <p class="hero-subtitle">Your Key to a Healthy Life!</p>
      <p class="hero-text">BreathTab alters your smoking routine and eases you off cigarettes gradually...</p>
      <a class="btn btn-green" href="#">Explore More</a>
    </div>
  </section>

  <section class="product">
    <div class="container">
      <div class="product-media">
        <div class="media-tab">BreathTab alters your smoking</div>
        <div class="product-photo" role="img" aria-label="Product photo placeholder: hand holding the BreathTab handheld timer device"></div>
      </div>
      <div class="product-info">
        <h2 class="product-title">Program by Velmora</h2>
        <p class="product-text">BreathTab alters your smoking routine and eases you off cigarettes gradually. BreathTab reminds you when to smoke and when not to smoke. Step by step, hour by hour. One day at a time.</p>
        <p class="price"><s>$99.95</s><span class="sale">$39.95 Sale</span></p>
        <div class="product-actions">
          <a class="btn btn-green" href="#">Add to Cart</a>
          <a class="btn btn-outline" href="#">View More</a>
        </div>
        <div class="share">Share <span class="sq"></span><span class="sq"></span><span class="sq"></span></div>
      </div>
    </div>
  </section>

  <section class="benefits">
    <h2 class="benefits-heading">Here's why BreathTab is the best way to<br>beat your tobacco addiction.</h2>
    <div class="benefit-card">
      <div class="benefit">
        <svg class="benefit-icon" viewBox="0 0 24 24" aria-hidden="true"><circle cx="12" cy="12" r="11" fill="#8cc63f"/><path d="M7 12.5l3 3 7-7" stroke="#fff" stroke-width="2.2" fill="none"/></svg>
        <div><h3>Step-by-Step Plan</h3><p>Cut down at your own pace.</p></div>
      </div>
      <div class="benefit">
        <svg class="benefit-icon" viewBox="0 0 24 24" aria-hidden="true"><circle cx="12" cy="12" r="11" fill="#8cc63f"/><path d="M7 12.5l3 3 7-7" stroke="#fff" stroke-width="2.2" fill="none"/></svg>
        <div><h3>No Withdrawal</h3><p>Ease off without cravings or stress.</p></div>
      </div>
      <div class="benefit">
        <svg class="benefit-icon" viewBox="0 0 24 24" aria-hidden="true"><circle cx="12" cy="12" r="11" fill="#8cc63f"/><path d="M7 12.5l3 3 7-7" stroke="#fff" stroke-width="2.2" fill="none"/></svg>
        <div><h3>Clinically Tested</h3><p>Backed by years of field research.</p></div>
      </div>
      <div class="benefit">
        <svg class="benefit-icon" viewBox="0 0 24 24" aria-hidden="true"><circle cx="12" cy="12" r="11" fill="#8cc63f"/><path d="M7 12.5l3 3 7-7" stroke="#fff" stroke-width="2.2" fill="none"/></svg>
        <div><h3>Fully Guided</h3><p>The device tells you when to smoke.</p></div>
      </div>
      <div class="benefit">
        <svg class="benefit-icon" viewBox="0 0 24 24" aria-hidden="true"><circle cx="12" cy="12" r="11" fill="#8cc63f"/><path d="M7 12.5l3 3 7-7" stroke="#fff" stroke-width="2.2" fill="none"/></svg>
        <div><h3>Proven Results</h3><p>Thousands have quit with this method.</p></div>
      </div>
      <div class="benefit">
        <svg class="benefit-icon" viewBox="0 0 24 24" aria-hidden="true"><circle cx="12" cy="12" r="11" fill="#8cc63f"/><path d="M7 12.5l3 3 7-7" stroke="#fff" stroke-width="2.2" fill="none"/></svg>
        <div><h3>Free Support Hotline</h3><p>Talk to our coaches any time.</p></div>
      </div>
    </div>
    <p class="how-title">How Does BreathTab Work</p>
  </section>

</div>
</body>
</html>
```